Website Design for a Project Management Consulting Business

I have a logo design already and now I need a website.
I am a project manager and run my own consulting business.
Currently I am under contract with 3 major Kestrelmark 300 companies. I'd like a website I can direct current and future clients.
My job is running IT projects and working with developers to deliver business priorities.
The website should be professional and clean - I work IT projects and would like to incorporate that into any theme.
I'd like the site to have several page or breakoff links - sections would include : about me, about my services, a page to display all of my certification badges, another page to talk about highlights from past projects and so on.
Looking for a collaborative experience.

Industry/Entity Type

Kestrelmark 300 Consulting Firm - Project Management

Coding

Coded - Design and coding required

Number of Pages Required

1 page

Font styles to use
Serif

Colors
0094D4
00A9DD
6FCCEA
C7EBF8
E9F6FB
EE7325
F08F49
F5BC92
FAE3D3
FDF4ED

Requirements
Must have
• Sections that are a must: About Me (bio), About My Services, About my Certifications and Credentials, Experience on Past Projects,
Nice to have
• I have added the logo below - I'd like to use the logo and have it prominent ; should be professional and inviting

```html
<!DOCTYPE html>
<html lang="en">
<head>
<meta charset="utf-8">
<title>Summitline Delivery LLC — Project Management Consulting</title>
<link rel="stylesheet" href="https://fonts.googleapis.com/css2?family=Barlow:wght@400;500;600&family=Barlow+Condensed:wght@500;600;700&display=swap">
<style>
:root{
  --navy:#0d2f55;
  --navy-deep:#0a3d78;
  --blue:#0094D4;
  --cyan:#00A9DD;
  --sky:#6FCCEA;
  --ice:#C7EBF8;
  --mist:#E9F6FB;
  --orange:#EE7325;
  --orange-soft:#F08F49;
  --peach:#FDF4ED;
  --ink:#2b3440;
  --white:#ffffff;
}
*{box-sizing:border-box;margin:0;padding:0}
html,body{width:1200px;height:3670px;overflow:hidden}
body{position:relative;background:var(--white);font-family:"Barlow",sans-serif;color:var(--ink)}
.cond{font-family:"Barlow Condensed",sans-serif}
.abs{position:absolute}
.accent{color:var(--cyan)}
.rule{position:absolute;height:2px;width:44px;background:var(--orange)}
.btn{position:absolute;display:flex;align-items:center;justify-content:center;background:var(--orange);color:var(--white);border-radius:24px;font-family:"Barlow Condensed",sans-serif;font-weight:700;letter-spacing:1.5px;font-size:17px}

/* header */
.site-header{position:absolute;left:0;top:0;width:1200px;height:100px;background:var(--white);box-shadow:0 1px 4px rgba(0,0,0,.08);z-index:2}
.brand{position:absolute;display:flex;align-items:center;gap:10px}
.brand-mark{width:40px;height:40px;background:var(--navy-deep)}
.brand-name{font-family:"Barlow Condensed",sans-serif;font-weight:700;font-size:30px;color:var(--navy-deep);letter-spacing:1px;line-height:1}
.top-contact{position:absolute;top:20px;right:24px;display:flex;gap:28px;font-family:"Barlow Condensed",sans-serif;font-weight:600;font-size:15px;color:var(--navy)}
.top-contact span{display:flex;align-items:center;gap:8px}
.main-nav{position:absolute;top:62px;right:24px;display:flex;gap:16px;font-size:12.5px;letter-spacing:1px;color:var(--navy);font-weight:500}
.main-nav a{color:inherit;text-decoration:none;display:flex;align-items:center;gap:8px}
.main-nav a::before{content:"";width:16px;height:2px;background:var(--cyan)}

/* hero */
.hero{position:absolute;left:0;top:100px;width:1200px;height:471px;background:linear-gradient(120deg,#0c57a6 0%,#0a3d78 100%);overflow:hidden}
.hero-circle{position:absolute;border-radius:50%;background:rgba(255,255,255,.12)}
.hero-title{position:absolute;left:157px;top:115px;font-family:"Barlow Condensed",sans-serif;font-weight:700;line-height:1;color:var(--white)}
.hero-title .l1{font-size:42px;display:block}
.hero-title .l2{font-size:56px;display:block;color:var(--cyan);margin-top:4px}
.hero-text{position:absolute;left:159px;top:229px;width:360px;color:var(--white);font-size:18px;line-height:1.45}
.hero-photo{position:absolute;left:600px;top:0;width:442px;height:471px;background:radial-gradient(circle at 50% 38%,#7a5a44 0%,#3a2a22 35%,#111 75%)}

/* section titles */
.sec-title{position:absolute;left:0;width:1200px;text-align:center;font-family:"Barlow Condensed",sans-serif;font-weight:700;font-size:48px;color:var(--navy);line-height:1}

/* services */
.service{position:absolute;width:279px;height:104px;border:2px solid var(--orange-soft);border-radius:4px;display:flex;align-items:center;justify-content:center;text-align:center;font-weight:600;font-size:18px;line-height:1.45;color:var(--navy)}

/* about */
.about-photo{position:absolute;left:158px;top:1089px;width:352px;height:508px;background:linear-gradient(180deg,#f2f4f6 0%,#e4e8ee 40%,#6d8db0 60%,#4f6f94 100%)}
.about-title{position:absolute;left:576px;top:1118px;font-family:"Barlow Condensed",sans-serif;font-weight:700;font-size:50px;color:var(--navy);line-height:1}
.about-text{position:absolute;left:576px;top:1214px;width:470px;font-size:15px;line-height:1.6;color:#3a3f47}
.about-text p+p{margin-top:24px}
.stat{position:absolute;font-family:"Barlow Condensed",sans-serif}
.stat b{display:block;font-size:32px;font-weight:600;color:var(--orange);line-height:1}
.stat span{display:block;font-size:17px;font-weight:600;color:var(--navy);margin-top:6px}

/* certifications */
.badge{position:absolute;width:90px;height:90px}
.badge .halo{position:absolute;left:38px;top:-12px;width:58px;height:58px;border-radius:50%;background:var(--mist)}
.badge .halo2{position:absolute;left:38px;top:46px;width:58px;height:58px;border-radius:50%;background:var(--mist)}
.badge .shape{position:absolute;left:8px;top:8px;width:74px;height:74px}

/* trusted */
.trusted{position:absolute;left:0;top:1982px;width:1200px;height:449px;background:var(--peach)}
.trusted-title{position:absolute;left:158px;top:60px;font-family:"Barlow Condensed",sans-serif;font-weight:700;font-size:48px;line-height:1.18;color:var(--navy)}
.trusted-text{position:absolute;left:158px;top:205px;width:375px;font-size:15.5px;line-height:1.55;color:#3a3f47}
.quote-name{position:absolute;left:158px;top:355px;font-weight:600;font-size:15px;color:var(--navy)}
.quote-role{position:absolute;left:158px;top:378px;font-size:15px;color:#3a3f47}
.quote-mark{position:absolute;left:476px;top:318px;font-family:"Barlow Condensed",sans-serif;font-weight:700;font-size:120px;line-height:1;color:var(--orange-soft)}
.trusted-photo{position:absolute;left:597px;top:0;width:443px;height:449px;background:linear-gradient(160deg,#d9dde2 0%,#9aa2ad 35%,#4a3a30 60%,#1e2430 100%)}

/* experience */
.exp-card{position:absolute;top:2608px;width:267px;height:202px;border:7px solid var(--ice);border-radius:4px}
.exp-photo{width:100%;height:100%}
.exp-caption{position:absolute;top:2840px;width:267px;text-align:center;font-weight:600;font-size:21px;line-height:1.35;color:var(--navy)}

/* contact */
.contact{position:absolute;left:0;top:2977px;width:1200px;height:443px;background:var(--cyan)}
.contact-title{position:absolute;left:158px;top:65px;font-family:"Barlow Condensed",sans-serif;font-weight:700;font-size:48px;color:var(--white);line-height:1}
.contact-rule{position:absolute;left:422px;top:100px;width:42px;height:2px;background:var(--orange)}
.contact-text{position:absolute;left:158px;top:132px;width:340px;font-size:15.5px;line-height:1.55;color:var(--white)}
.contact-line{position:absolute;left:158px;display:flex;gap:12px;font-family:"Barlow Condensed",sans-serif;font-size:19px;color:var(--white);line-height:1.35}
.contact-line .ico{width:26px;height:26px;flex:none;border-radius:50%;background:var(--white);display:flex;align-items:center;justify-content:center}
.contact-line b{font-weight:600}
.contact-line u{font-weight:500}
.field{position:absolute;height:38px;border:1.5px solid rgba(255,255,255,.85);border-radius:3px;padding:0 14px;display:flex;align-items:center;font-family:"Barlow Condensed",sans-serif;font-size:14px;letter-spacing:.5px;color:var(--white)}
.field.msg{align-items:flex-start;padding-top:12px;height:104px}

/* footer */
.footer-head{position:absolute;top:3486px;font-family:"Barlow Condensed",sans-serif;font-weight:700;font-size:21px;color:var(--navy)}
.footer-list{position:absolute;top:3523px;font-size:12px;line-height:24px;color:#3a3f47;list-style:none}
.social{position:absolute;top:3565px;left:816px;display:flex;gap:16px}
.social span{width:18px;height:18px;border-radius:50%;background:var(--blue)}
.copyright{position:absolute;left:721px;top:3606px;font-size:12px;color:#3a3f47}
</style>
</head>
<body>

<header class="site-header">
  <div class="brand" style="left:24px;top:30px">
    <div class="brand-mark"></div>
    <div class="brand-name">SUMMITLINE DELIVERY</div>
  </div>
  <div class="top-contact">
    <span><svg width="15" height="15" viewBox="0 0 24 24" fill="none" stroke="#EE7325" stroke-width="2"><path d="M5 3h4l2 5-3 2a11 11 0 0 0 6 6l2-3 5 2v4a2 2 0 0 1-2 2A17 17 0 0 1 3 5a2 2 0 0 1 2-2z"/></svg>Call Me - (555) 014-2290</span>
    <span><svg width="16" height="13" viewBox="0 0 24 18" fill="none" stroke="#EE7325" stroke-width="2"><rect x="1" y="1" width="22" height="16"/><path d="M1 1l11 9 11-9"/></svg>Emai Me - hello@summitlinedelivery.com</span>
  </div>
  <nav class="main-nav">
    <a href="#about">ABOUT ME</a>
    <a href="#services">MY SERVICES</a>
    <a href="#certs">CERTIFICATIONS AND CREDENTIALS</a>
    <a href="#experience">EXPERIENCE</a>
    <a href="#contact">CONTACT</a>
  </nav>
</header>

<section class="hero">
  <div class="hero-circle" style="left:-80px;top:355px;width:210px;height:210px"></div>
  <div class="hero-circle" style="left:505px;top:300px;width:90px;height:90px"></div>
  <div class="hero-circle" style="left:1000px;top:58px;width:140px;height:140px"></div>
  <div class="hero-circle" style="left:1100px;top:150px;width:90px;height:90px"></div>
  <h1 class="hero-title"><span class="l1">EXTENSIVE EXPERIENCED</span><span class="l2">CONSULTANT</span></h1>
  <p class="hero-text">Serves as Principal Lead Consultant on waterfall and agile contract opportunities.</p>
  <div class="btn" style="left:158px;top:306px;width:184px;height:42px">MY EXPERIENCE</div>
  <div class="hero-photo" role="img" aria-label="Portrait photo of the consultant in a pinstripe suit on a dark background"></div>
</section>

<section id="services">
  <h2 class="sec-title" style="top:655px">ABOUT <span class="accent">MY SERVICES</span></h2>
  <div class="rule" style="left:547px;top:723px"></div>
  <div class="service" style="left:158px;top:767px">LEADING SAFE AGILE<br>SCRUM TEAMS</div>
  <div class="service" style="left:459px;top:767px">LEADING SAFE AGILE<br>SCRUM TEAMS</div>
  <div class="service" style="left:761px;top:767px">LEADING SAFE AGILE<br>SCRUM TEAMS</div>
  <div class="service" style="left:158px;top:895px">LEADING SAFE AGILE<br>SCRUM TEAMS</div>
  <div class="service" style="left:459px;top:895px">LEADING SAFE AGILE<br>SCRUM TEAMS</div>
  <div class="service" style="left:761px;top:895px">LEADING SAFE AGILE<br>SCRUM TEAMS</div>
</section>

<section id="about">
  <div class="about-photo" role="img" aria-label="Full-length photo of the consultant in a blue plaid blazer and lilac tie"></div>
  <h2 class="about-title">ABOUT <span class="accent">ME</span></h2>
  <div class="rule" style="left:576px;top:1186px"></div>
  <div class="about-text">
    <p>Marcus Ellery is the Owner of Summitline Delivery, LLC and serves as Principal Lead Consultant on waterfall and agile contract opportunities.</p>
    <p>Summitline Delivery, LLC has engaged on a contract basis with Kestrelmark 300 companies across various industries including banking and credit unions, global supply chain, and international food distribution. Marcus Ellery brings 12 years of experience to his clients encompassing various project methodologies including: waterfall, agile, and hybrid frameworks.</p>
  </div>
  <div class="stat" style="left:576px;top:1472px"><b>500+</b><span>Satisfied Clients</span></div>
  <div class="stat" style="left:748px;top:1472px"><b>99%</b><span>Success of Works</span></div>
  <div class="btn" style="left:572px;top:1557px;width:152px;height:42px">KNOW MORE</div>
</section>

<section id="certs">
  <h2 class="sec-title" style="top:1678px">CERTIFICATIONS <span class="accent">&amp; CREDENTIALS</span></h2>
  <div class="rule" style="left:547px;top:1745px"></div>
  <svg class="abs" style="left:156px;top:1817px" width="22" height="40" viewBox="0 0 22 40" fill="none" stroke="#EE7325" stroke-width="2.5"><path d="M20 2L3 20l17 18"/></svg>
  <svg class="abs" style="left:1020px;top:1817px" width="22" height="40" viewBox="0 0 22 40" fill="none" stroke="#EE7325" stroke-width="2.5"><path d="M2 2l17 18L2 38"/></svg>

  <div class="badge" style="left:205px;top:1792px"><div class="halo2"></div><svg class="shape" viewBox="0 0 74 74"><circle cx="37" cy="37" r="35" fill="#fff" stroke="#5b2c83" stroke-width="4"/></svg></div>
  <div class="badge" style="left:343px;top:1792px"><div class="halo"></div><svg class="shape" viewBox="0 0 74 74"><circle cx="37" cy="37" r="35" fill="#fff" stroke="#5b2c83" stroke-width="4"/></svg></div>
  <div class="badge" style="left:481px;top:1792px"><div class="halo2"></div><svg class="shape" viewBox="0 0 74 74"><path d="M37 2l35 35-35 35L2 37z" fill="#1d3c5c"/></svg></div>
  <div class="badge" style="left:619px;top:1792px"><div class="halo"></div><svg class="shape" viewBox="0 0 74 74"><path d="M37 2l35 35-35 35L2 37z" fill="#1d3c5c"/></svg></div>
  <div class="badge" style="left:757px;top:1792px"><div class="halo2"></div><svg class="shape" viewBox="0 0 74 74"><circle cx="37" cy="37" r="33" fill="#EE7325"/></svg></div>
  <div class="badge" style="left:895px;top:1792px"><div class="halo"></div><svg class="shape" viewBox="0 0 74 74"><circle cx="37" cy="37" r="33" fill="#f2a81d"/></svg></div>
</section>

<section class="trusted">
  <h2 class="trusted-title">TRUSTED BY BIGGEST<br><span class="accent">BUSINESS NAMES</span></h2>
  <div class="rule" style="left:158px;top:178px"></div>
  <p class="trusted-text">Lorem ipsum dolor sit amet, consectetur adipiscing elit, sed do eiusmod tempor incididunt ut labore et dolore magna aliqua. Ut enim ad minim veniam, quis nostrud exercitation ullamco laboris nisi ut aliquip ex ea commodo consequat.</p>
  <div class="quote-name">DANIEL OKORO</div>
  <div class="quote-role">Brightwell Startup</div>
  <div class="quote-mark">”</div>
  <div class="trusted-photo" role="img" aria-label="Photo of the consultant in an office with a dashboard screen behind"></div>
</section>

<section id="experience">
  <h2 class="sec-title" style="top:2516px;color:var(--cyan)">EXPERIENCE</h2>
  <div class="rule" style="left:577px;top:2577px"></div>
  <div class="exp-card" style="left:160px"><div class="exp-photo" role="img" aria-label="Photo of the consultant indoors in a tan jacket" style="background:linear-gradient(180deg,#c9bfb4,#6b5141)"></div></div>
  <div class="exp-card" style="left:467px"><div class="exp-photo" role="img" aria-label="Photo of the consultant in a blue blazer on a light background" style="background:linear-gradient(180deg,#eef0f2,#7e9ab8)"></div></div>
  <div class="exp-card" style="left:774px"><div class="exp-photo" role="img" aria-label="Photo of the consultant in a pinstripe suit on a dark background" style="background:linear-gradient(180deg,#1b1b1b,#4a3a30)"></div></div>
  <div class="exp-caption" style="left:160px">SENIOR SAFE SCRUM<br>MASTER</div>
  <div class="exp-caption" style="left:467px">SENIOR PROJECT<br>MANGER</div>
  <div class="exp-caption" style="left:774px">SENIOR PROGRAM<br>MANGER</div>
</section>

<section class="contact" id="contact">
  <h2 class="contact-title">GET IN TOUCH</h2>
  <div class="contact-rule"></div>
  <p class="contact-text">We're glad to discuss your organisation's situation. So please contact us via the details below, or enter your request.</p>
  <div class="contact-line" style="top:226px">
    <span class="ico"><svg width="12" height="14" viewBox="0 0 12 16"><path d="M6 0a6 6 0 0 0-6 6c0 4 6 10 6 10s6-6 6-10a6 6 0 0 0-6-6z" fill="#00A9DD"/><circle cx="6" cy="6" r="2" fill="#fff"/></svg></span>
    <span>Address -</span><span>48 Larkfield Row,<br>NY, 10099, USA.</span>
  </div>
  <div class="contact-line" style="top:284px">
    <span class="ico"><svg width="13" height="13" viewBox="0 0 24 24"><path d="M5 3h4l2 5-3 2a11 11 0 0 0 6 6l2-3 5 2v4a2 2 0 0 1-2 2A17 17 0 0 1 3 5a2 2 0 0 1 2-2z" fill="#00A9DD"/></svg></span>
    <span>Call Me -</span><b>(555) 014-2290</b>
  </div>
  <div class="contact-line" style="top:318px">
    <span class="ico"><svg width="13" height="10" viewBox="0 0 24 18" fill="none" stroke="#00A9DD" stroke-width="2.5"><rect x="1" y="1" width="22" height="16"/><path d="M1 1l11 9 11-9"/></svg></span>
    <span>Emai Me -</span><u>hello@summitlinedelivery.com</u>
  </div>

  <div class="field" style="left:538px;top:66px;width:241px">FIRST NAME</div>
  <div class="field" style="left:799px;top:66px;width:241px">LAST NAME</div>
  <div class="field" style="left:538px;top:122px;width:241px">EMAIL ADDRESS</div>
  <div class="field" style="left:799px;top:122px;width:241px">PHONE</div>
  <div class="field" style="left:538px;top:178px;width:241px">WEBSITE</div>
  <div class="field" style="left:799px;top:178px;width:241px">SERVICES</div>
  <div class="field msg" style="left:538px;top:234px;width:500px">MESSAGE</div>
  <div class="btn" style="left:857px;top:356px;width:180px;height:42px">SEND REQUEST</div>
</section>

<footer>
  <div class="footer-head" style="left:158px">USEFULL LINKS</div>
  <ul class="footer-list" style="left:158px">
    <li>- About Me</li><li>- Experience</li><li style="line-height:16px;padding:4px 0">- Certifications and<br>&nbsp;&nbsp;Credentials</li><li>- Contact Us</li>
  </ul>
  <ul class="footer-list" style="left:310px">
    <li>- Privacy Policy</li><li>- Terms &amp; Conditions</li>
  </ul>
  <div class="footer-head" style="left:481px">SERVICES</div>
  <ul class="footer-list" style="left:481px">
    <li>- Services1</li><li>- Services1</li><li>- Services1</li><li>- Services1</li>
  </ul>
  <div class="brand" style="left:728px;top:3490px">
    <div class="brand-mark"></div>
    <div class="brand-name">SUMMITLINE DELIVERY</div>
  </div>
  <div class="social"><span></span><span></span><span></span><span></span></div>
  <div class="copyright">Copyright © 2022 SUMMITLINE DELIVERY LLC. All rights reserved.</div>
</footer>

</body>
</html>
```